Radiology Department needs a series of 3 facebook posts - similar design

We need a series of 3 posts for our facebook page, each one presenting the activity of one of 3 physicians.
The main design elements can be the same, the only thing that will change between posts will be the field of activity and name of the physician and the representative image of its activity.
If needed the design elements can be slightly different between posts for better adjustment to the representative images.
You can find as an attachment:
- Manual of institutional identity of the Hospital (Velmor Clinica)
- Our facebook cover page
- Our department video
- The representative images for each post, identified with the name of each physician
- The Institutional identity manual with the logo of "Brisa Medical School" - just for Dr Tomas Brandilo post.
So, each one of the three posts should state the name and field of activity of each physician, including somehow the corresponding representative image, and should have background innovative design elements.
Post 1:
Name of the physician: Prof. Doutor Rui Castelvo
Field of activity: Imagiologia Reumatológica e do Sistema Músculo-Esquelético
Image as an attachment
Post 2:
Name of the physician: Prof.ª Doutora Inês Barroca
Field of activity: Imagiologia Cardíaca
Image as an attachment
Post 3:
Name of the physician: Dr. Tomas Lupo
Field of activity: Tese de Doutoramento em Curso - Identificação da Lesão Cartilagínea Precoce. Com orientação do Prof. Doutor Rui Castelvo e Prof.ª Doutora Inês Sofia Carvalhal.
Image as an attachment
Just for Dr Tomas Lupo, the logo of Brisa Medical School should also be included (please check the corresponding institutional identity manual that was just added in documents).
Updates

Just for Dr Tomas Brandilo, the logo of Brisa Medical School should also be included (please check the corresponding institutional identity manual that was just added in documents).

Please note that we are just looking for 3 facebook POSTS, not facebook cover page, thanks.

Please kindly note that we are looking for facebook POST and NOT facebook cover page.

Target Market(s)

General Population

Industry/Entity Type

Health

Font styles to use
Other font styles liked:
• Check manual of institutional identity and try to approach if appropriate

Requirements
Must have
• Check project description.
Nice to have
• If the designer finds appropriate, the logo of the Hospital would be nice in all the three posts, the most simple one just stating "VelmorClinica" - please check the attached manual of institutional identity

```html
<!DOCTYPE html>
<html lang="pt">
<head>
<meta charset="utf-8">
<title>Radiologia — série de publicações</title>
<link href="https://fonts.googleapis.com/css2?family=Montserrat:wght@600;800&family=Roboto:wght@300&family=Roboto+Condensed:wght@400&display=swap" rel="stylesheet">
<style>
  :root{
    --page:#f0f0f0;
    --teal:#0b5e6b;
    --teal-deep:#08525e;
    --teal-light:#0f7284;
    --yellow:#fbb52a;
    --orange:#e89b22;
    --white:#ffffff;
    --ink:#1b1b1b;
    --label:#1a1a1a;
  }
  *{margin:0;padding:0;box-sizing:border-box}
  html,body{width:1200px;height:2188px;overflow:hidden;background:var(--page)}
  .sheet{position:relative;width:1200px;height:2188px}
  .series-label{
    position:absolute;left:185px;width:300px;text-align:center;
    font:300 48px/1 "Roboto",sans-serif;color:var(--label);
    transform:translate(-50%,-50%) rotate(-90deg);white-space:nowrap;
  }
  .post{position:absolute;left:295px;width:611px;height:611px;overflow:hidden;background:var(--white)}
  .post svg.backdrop{position:absolute;inset:0;width:611px;height:611px}
  .physician{
    position:absolute;left:58px;top:44px;
    font:800 53px/52px "Montserrat",sans-serif;color:var(--teal);letter-spacing:-0.3px;
  }
  .field{
    position:absolute;left:0;background:var(--yellow);
    border-radius:0 40px 40px 0;padding:0 20px 0 58px;
    display:flex;align-items:center;
    font:600 18.5px/30px "Montserrat",sans-serif;color:var(--ink);
  }
  .brand{position:absolute;left:383px;top:519px;display:flex;align-items:center;gap:6px}
  .brand-dot{width:40px;height:40px;border-radius:50%;background:var(--white)}
  .brand-name{font:600 24px/1 "Montserrat",sans-serif;color:var(--white)}
  .brand-tagline{position:absolute;left:428px;top:562px;font:400 10.5px/1 "Roboto Condensed",sans-serif;color:var(--white)}
</style>
</head>
<body>
<div class="sheet">

  <span class="series-label" style="top:436px">Banner 01</span>
  <span class="series-label" style="top:1099px">Banner 02</span>
  <span class="series-label" style="top:1762px">Banner 03</span>

  <!-- Post 1 -->
  <section class="post" style="top:131px">
    <svg class="backdrop" viewBox="0 0 611 611" aria-hidden="true">
      <defs>
        <radialGradient id="scan-hands" cx="50%" cy="45%" r="55%">
          <stop offset="0" stop-color="#9a9a9a"/><stop offset="0.55" stop-color="#4a4a4a"/><stop offset="1" stop-color="#050505"/>
        </radialGradient>
      </defs>
      <path d="M611,290 C520,420 420,440 320,450 L290,611 L611,611 Z" fill="var(--teal)"/>
      <path d="M611,470 C520,500 430,540 330,611 L611,611 Z" fill="var(--teal-light)" opacity="0.55"/>
      <path d="M520,0 L611,0 L611,300 C540,420 430,440 320,445 Z" fill="var(--yellow)"/>
      <path d="M520,0 L570,0 C600,70 600,170 585,230 C555,350 450,430 320,442 Z" fill="var(--orange)"/>
      <path d="M0,0 L520,0 C555,60 565,130 563,190 C558,330 450,430 320,440 L0,440 Z" fill="var(--white)"/>
      <circle cx="130" cy="497" r="208" fill="var(--white)"/>
      <circle cx="130" cy="497" r="200" fill="url(#scan-hands)" role="img" aria-label="Angiografia por ressonância das duas mãos em tons de cinzento"/>
    </svg>
    <h1 class="physician">Prof. Doutor<br>Rui Castelvo</h1>
    <p class="field" style="top:161px;height:78px;width:417px">Imagiologia Reumatológica e do<br>Sistema Músculo-Esquelético</p>
    <div class="brand"><span class="brand-dot"></span><span class="brand-name">VelmorClinica</span></div>
    <p class="brand-tagline">Construímos relações de confiança</p>
  </section>

  <!-- Post 2 -->
  <section class="post" style="top:794px">
    <svg class="backdrop" viewBox="0 0 611 611" aria-hidden="true">
      <defs>
        <radialGradient id="scan-heart" cx="40%" cy="55%" r="55%">
          <stop offset="0" stop-color="#7a1f16"/><stop offset="0.5" stop-color="#4a1410"/><stop offset="1" stop-color="#050505"/>
        </radialGradient>
      </defs>
      <path d="M611,290 C520,420 420,440 320,450 L290,611 L611,611 Z" fill="var(--teal)"/>
      <path d="M611,470 C520,500 430,540 330,611 L611,611 Z" fill="var(--teal-light)" opacity="0.55"/>
      <path d="M520,0 L611,0 L611,300 C540,420 430,440 320,445 Z" fill="var(--yellow)"/>
      <path d="M520,0 L570,0 C600,70 600,170 585,230 C555,350 450,430 320,442 Z" fill="var(--orange)"/>
      <path d="M0,0 L520,0 C555,60 565,130 563,190 C558,330 450,430 320,440 L0,440 Z" fill="var(--white)"/>
      <circle cx="130" cy="497" r="208" fill="var(--white)"/>
      <circle cx="130" cy="497" r="200" fill="url(#scan-heart)" role="img" aria-label="Reconstrução 3D do coração com artérias coronárias"/>
    </svg>
    <h1 class="physician">Prof.ª Doutora<br>Inês Barroca</h1>
    <p class="field" style="top:161px;height:51px;width:290px">Imagiologia Cardíaca</p>
    <div class="brand"><span class="brand-dot"></span><span class="brand-name">VelmorClinica</span></div>
    <p class="brand-tagline">Construímos relações de confiança</p>
  </section>

  <!-- Post 3 -->
  <section class="post" style="top:1457px">
    <svg class="backdrop" viewBox="0 0 611 611" aria-hidden="true">
      <defs>
        <radialGradient id="scan-knee" cx="50%" cy="50%" r="55%">
          <stop offset="0" stop-color="#1f3aa8"/><stop offset="0.6" stop-color="#2b4fd0"/><stop offset="1" stop-color="#15246e"/>
        </radialGradient>
      </defs>
      <path d="M611,290 C520,420 420,440 320,450 L290,611 L611,611 Z" fill="var(--teal)"/>
      <path d="M611,470 C520,500 430,540 330,611 L611,611 Z" fill="var(--teal-light)" opacity="0.55"/>
      <path d="M520,0 L611,0 L611,300 C540,420 430,440 320,445 Z" fill="var(--yellow)"/>
      <path d="M520,0 L570,0 C600,70 600,170 585,230 C555,350 450,430 320,442 Z" fill="var(--orange)"/>
      <path d="M0,0 L520,0 C555,60 565,130 563,190 C558,330 450,430 320,440 L0,440 Z" fill="var(--white)"/>
      <circle cx="130" cy="497" r="208" fill="var(--white)"/>
      <circle cx="130" cy="497" r="200" fill="url(#scan-knee)" role="img" aria-label="Mapa paramétrico de ressonância da cartilagem do joelho em tons de azul"/>
    </svg>
    <h1 class="physician">Dr. Tomas Lupo</h1>
    <p class="field" style="top:114px;height:148px;width:533px">Tese de Doutoramento em Curso - Identifi-<br>cação da Lesão Cartilagínea Precoce. Com<br>orientação do Prof. Doutor Rui Castelvo e<br>Prof.ª Doutora Inês Sofia Carvalhal</p>
    <div class="brand"><span class="brand-dot"></span><span class="brand-name">VelmorClinica</span></div>
    <p class="brand-tagline">Construímos relações de confiança</p>
  </section>

</div>
</body>
</html>
```